International education charity requires an A4, 8-10 page brochure

Lantern Grove Foundation is a charity that builds schools and educates hundreds of children living in poverty in Uganda. We are expanding our child sponsorship program and are putting together a printed A4 Welcome Pack, that provides people who sponsor a child with our history, how child sponsorship works and a day in the life of a child. All low res images and text is provided - documented as Welcome Pack - final , as well as some examples of our brand style - LGF Ball sponsorship, lantern grove brochure, Tavo poster and a brand story document for background.

Target Market(s)

Caring individuals who have signed up for child sponsorship at Lantern Grove. Married women with school-age children make up most of our audience, although wealthy males are also included in this.

Industry/Entity Type

Charity

Other font styles liked:
• Neutra Text - TF Light

Colors
0492cd
cee9f5
85cae6
33a6d7
ecf7fb
ffffff

Requirements
Must have
• Project must be in accordance to Lantern Grove's brand style and colours as seen in the Brand Story document. Led by graphics, with easy to read text weaved into the format of the brochure. The story of Miriam at the end should be emotive and powerful. The document should be simple but modern.
Nice to have
• Our current website is being updated, but the link for more images are background is www.lanterngrovetrust.org.au
Should not have
• Should not have unbranded colours.

```html
<!DOCTYPE html>
<html lang="en">
<head>
<meta charset="utf-8">
<title>Welcome Pack – A Day in the Life</title>
<link href="https://fonts.googleapis.com/css2?family=Montserrat:wght@800&display=swap" rel="stylesheet">
<style>
  :root{
    --backdrop:#ececec;
    --ink:#ffffff;
    --rule:#e4e4e4;
    --tone-leaf:#4f7a6a;
    --tone-sky:#5b8fa8;
    --tone-slate:#3f6d8c;
    --tone-dusk:#7c7a8c;
    --tone-clay:#c99a7c;
    --tone-sand:#e6b78f;
  }
  *{margin:0;padding:0;box-sizing:border-box}
  html,body{width:1200px;height:833px;overflow:hidden;background:var(--backdrop)}
  .spread{
    position:absolute;left:105px;top:66px;
    width:990px;height:700px;display:flex;
    box-shadow:0 12px 30px rgba(0,0,0,.18);
  }
  .page{position:relative;width:495px;height:700px;overflow:hidden}
  .photo{position:absolute;inset:0}
  .page--left .photo{
    background:
      radial-gradient(ellipse 30% 22% at 62% 24%, rgba(120,90,70,.55), transparent 70%),
      linear-gradient(180deg,var(--tone-leaf) 0%,var(--tone-sky) 30%,var(--tone-slate) 55%,var(--tone-dusk) 75%,var(--tone-clay) 100%);
  }
  .page--right .photo{
    background:
      linear-gradient(180deg,#5f6e55 0%,#6f7f6a 22%,var(--tone-sky) 42%,var(--tone-dusk) 62%,var(--tone-clay) 82%,var(--tone-sand) 100%);
  }
  .gutter{position:absolute;top:0;bottom:0;width:40px;pointer-events:none}
  .page--left .gutter{right:0;background:linear-gradient(90deg,transparent,rgba(0,0,0,.18))}
  .page--right .gutter{left:0;background:linear-gradient(270deg,transparent,rgba(0,0,0,.2))}
  .story{
    position:absolute;color:var(--ink);
    font-family:"Montserrat",sans-serif;font-weight:800;
    text-transform:uppercase;font-size:22px;line-height:1.22;letter-spacing:.5px;
  }
  .story::before{
    content:"";position:absolute;left:-40px;top:-2px;bottom:-40px;width:20px;background:var(--rule);
  }
  .page--left .story{left:80px;top:270px;width:385px}
  .page--right .story{left:44px;top:150px;width:425px}
  .page--right .story::before{left:-44px;width:14px;bottom:-2px}
</style>
</head>
<body>
  <main class="spread">
    <section class="page page--left">
      <div class="photo" role="img" aria-label="Photograph of a smiling schoolgirl in uniform seated outdoors in front of blurred trees"></div>
      <p class="story">Miriam wakes at 6am and walks for two hours to get to school for Lantern Grove's Willowmere campus, where she is given breakfast. She is 14 years-old, although as her mother is illiterate she wasn't able to keep track of her exact birthday so this is an estimate.</p>
      <div class="gutter"></div>
    </section>
    <section class="page page--right">
      <div class="photo" role="img" aria-label="Photograph of a group of children playing on a dirt path beneath banana trees"></div>
      <p class="story">Miriam is the second-youngest child out of 11 siblings. She lives with her mother Agnes, her older sister and her sister's baby, her older brother and his son, and her younger sister. Her father has remarried and has another six children.</p>
      <div class="gutter"></div>
    </section>
  </main>
</body>
</html>
```